Scientific Web Site for TRELDMIST

Professional Scientific / Service orientated web site, motto, new logos attached for viewing.

"We measure so the Business Owner can Manage" their environments.
Site needs to be be mobile friendly.

We provide a service to electronically measure cleanliness of any surface and a value added disinfecting fogging surface.

Reports showing locations, trending, tracking and randomized test plans ongoing audits will be made available..

NOTE: Although image of Corona Virus is current we don't wont it plastered through the web site, their is more than the current virus.

Home Page - Professional Scientific / Service Looking
About
Our Approach
Services
Residential
Commercial
Transportation
Gyms
Educational & Daycare
Real Estate - Open for inspections, End of Lease etc

Contact
Mobile #
Email
Form to leave their details

Links to social media, Facebook, Instagram
Reference Sites: Ranked in preference
www.orlimber.com.au
https://www.brightquarrymethods.co.uk/
https://www.vantopel.com/
https://www.kwtpure.com.au/specialist-surface-disinfection/
https://www.artmosaicly.com/design/48102957
https://www.artmosaicly.com/design/48736614
https://www.artmosaicly.com/design/48029561

Target Market(s)

Commercial and professional Services

Font styles to use
Sans Serif

Requirements
Must have
• Wix Website
Clean fresh look with appropriate imaging
Web site is a company advertising that will hold static information and we will market through social media.
Nice to have
• Scientific look and feel
Should not have
• Prominent Corona Virus images or references

```html
<!DOCTYPE html>
<html lang="en">
<head>
<meta charset="utf-8">
<title>TRELDMIST — We measure so the Business Owner can Manage</title>
<link rel="stylesheet" href="https://fonts.googleapis.com/css2?family=Outfit:wght@300;400;500;600;700;800&display=swap">
<style>
:root{
  --orange:#f26522;
  --dark:#1d1a1b;
  --ink:#1b1b1b;
  --body:#333;
  --white:#fff;
  --dot:#cfcfcf;
  --line:#d9d9d9;
}
*{box-sizing:border-box;margin:0;padding:0}
html,body{width:1200px;height:3974px;overflow:hidden}
body{font-family:"Outfit",sans-serif;color:var(--body);background:var(--white);position:relative}
section,header,footer{position:absolute;left:0;width:1200px}
.abs{position:absolute}
.center{text-align:center;left:0;width:1200px}

/* hero */
.hero{top:0;height:714px;background:linear-gradient(100deg,#2a2a2c 0%,#4a4b4e 35%,#6d6c69 60%,#3a3838 100%)}
.logo{position:absolute;display:flex;align-items:center;gap:10px;font-weight:500;letter-spacing:3px}
.logo .mark{width:14px;height:14px;border-radius:50%;background:var(--orange)}
.hero .logo{left:74px;top:82px;color:var(--white);font-size:27px}
.nav{position:absolute;top:65px;left:570px;display:flex;font-size:15px;font-weight:500;color:var(--white)}
.nav a{color:inherit;text-decoration:none;padding:6px 20px 6px 0;line-height:20px}
.nav .active{background:var(--orange);padding:6px 21px;margin-right:17px}
.nav .caret{font-size:10px;margin-left:5px}
.hero h1{top:345px;font-size:45px;font-weight:600;line-height:54px;color:var(--white)}

/* about */
.about{top:714px;height:424px;background:linear-gradient(200deg,rgba(196,160,235,.35) 0%,rgba(255,255,255,0) 30%),var(--white)}
h2{font-weight:600;color:var(--ink)}
.about h2{top:58px;font-size:44px}
.about .lead{top:130px;font-size:16px;color:var(--orange)}
.para{font-size:15px;line-height:28.5px;color:var(--body)}
.about .p1{top:172px;left:160px;width:880px;text-align:center}
.about .p2{top:299px;left:160px;width:880px;text-align:center}

.dots{position:absolute;left:1140px;display:flex;flex-direction:column;gap:19px}
.dots i{width:12px;height:12px;border-radius:50%;background:var(--dot);display:block}
.dots i.on{background:var(--orange)}
.dots.light i{background:var(--white)}

/* services */
.services{top:1138px;height:466px;background:var(--dark);color:var(--white)}
.services h2{top:58px;font-size:44px;color:var(--white)}
.services .sub{top:132px;font-size:16px}
.service{position:absolute;top:180px;width:300px;text-align:center}
.service svg{display:block;margin:0 auto}
.service h3{margin-top:30px;font-size:22px;font-weight:600;color:var(--orange)}
.service p{margin:8px auto 0;width:275px;font-size:14px;line-height:28px}
.arrow{position:absolute;top:272px}

/* approach */
.approach{top:1604px;height:516px;background:linear-gradient(90deg,rgba(200,150,230,.25) 0%,rgba(255,255,255,0) 18%),var(--white)}
.approach .photo{left:74px;top:69px;width:512px;height:378px;background:linear-gradient(135deg,#2f3d55 0%,#6a7689 40%,#b9bcc2 60%,#3b4454 100%)}
.approach h2{left:614px;top:114px;font-size:44px}
.approach .p1{left:614px;top:185px;width:500px}
.approach .p2{left:614px;top:308px;width:500px}

/* banner */
.banner{top:2120px;height:421px;background:linear-gradient(90deg,#2c6b2a 0%,#4f7a2f 14%,#a2501c 42%,#d46a1c 70%,#c05a15 100%);color:var(--white)}
.banner h2{top:104px;font-size:31px;line-height:34px;color:var(--white)}
.banner .para{top:203px;left:160px;width:880px;text-align:center;color:var(--white)}

/* testimonials */
.reviews{top:2541px;height:602px;background:var(--white)}
.reviews h2{top:52px;font-size:44px}
.reviews .sub{top:126px;font-size:15px}
.card{position:absolute;top:187px;width:330px;height:253px;border:1px solid var(--line);text-align:center;padding:26px 22px 0}
.card .q{height:42px;display:flex;justify-content:center}
.card p{margin-top:22px;font-size:14.5px;line-height:28px}
.who{position:absolute;top:467px;width:330px;text-align:center}
.who b{display:block;font-size:16px;font-weight:500;color:var(--ink)}
.who .stars{margin-top:3px;font-size:17px;letter-spacing:2px;color:var(--orange)}

/* contact */
.contact{top:3143px;height:566px;background:linear-gradient(135deg,#1e2834 0%,#2d3a48 45%,#1c2430 100%);color:var(--white)}
.contact h2{top:52px;font-size:44px;color:var(--white)}
.contact .line{top:131px;font-size:14px;display:flex;justify-content:center;gap:12px;align-items:center}
.field{position:absolute;left:299px;width:602px;background:var(--white);color:#555;font-size:12px;padding:10px 14px}
.submit{position:absolute;left:524px;top:465px;width:151px;height:37px;background:var(--orange);color:var(--white);font-size:18px;font-weight:500;text-align:center;line-height:37px}

/* footer */
.foot{top:3709px;height:265px;background:var(--white)}
.foot .logo{left:77px;top:84px;color:var(--ink);font-size:28px}
.foot .col{position:absolute;font-size:14px;line-height:25px;color:var(--body)}
.foot .social{position:absolute;left:922px;top:70px;display:flex;gap:18px}
.foot .social i{display:block;width:18px;height:18px;border:2px solid #444;border-radius:3px}
.foot .copy{top:218px;font-size:12.5px}
</style>
</head>
<body>

<header class="hero">
  <div class="abs" role="img" aria-label="Photo of a technician in protective suit fogging a gym with a backpack sprayer" style="inset:0"></div>
  <div class="logo"><span class="mark"></span>TRELDMIST</div>
  <nav class="nav">
    <a class="active">Home</a><a>About</a><a>Our Approach</a><a>Services<span class="caret">&#8964;</span></a><a>Contact Us</a>
  </nav>
  <h1 class="abs center">We measure so the Business Owner can<br>Manage their Environments.</h1>
</header>

<section class="about">
  <h2 class="abs center">About TRELDMIST</h2>
  <p class="abs center lead">We provide a service to electronically measure cleanliness of any surface and a value added disinfecting fogging surface.</p>
  <p class="abs para p1">Lorem ipsum dolor sit amet, consectetur adipiscing elit. Integer auctor feugiat libero vitae tincidunt. Ut varius malesuada ex at porta. Quisque augue mauris, dignissim sed velit eget, finibus porta urna. Suspendisse eget tempor risus, et imperdiet nisi. Proin rhoncus, tellus sagittis rutrum aliquam, est ipsum vestibulum leo, vel tempor orci lacus ut nunc. Vivamus aliquet lectus nisl, vitae efficitur nisl dignissim quis.</p>
  <p class="abs para p2">Class aptent taciti sociosqu ad litora torquent per conubia nostra, per inceptos himenaeos. Sed cursus turpis sed lectus interdum, sed ullamcorper nunc malesuada. Sed nec est vel arcu sodales egestas sit amet vel nulla.</p>
  <div class="dots" style="top:152px"><i class="on"></i><i></i><i></i><i></i><i></i></div>
</section>

<section class="services">
  <h2 class="abs center">Our Services</h2>
  <p class="abs center sub">Morbi id congue nibhhasellus maximus nisl ante, ut dictum felis.</p>
  <svg class="arrow" style="left:72px" width="16" height="24" viewBox="0 0 16 24"><path d="M12 3 L4 12 L12 21" fill="none" stroke="#fff" stroke-width="3"/></svg>
  <svg class="arrow" style="left:1112px" width="16" height="24" viewBox="0 0 16 24"><path d="M4 3 L12 12 L4 21" fill="none" stroke="#fff" stroke-width="3"/></svg>
  <div class="service" style="left:89px">
    <svg width="64" height="62" viewBox="0 0 64 62" fill="none" stroke="#fff" stroke-width="2.5"><path d="M4 30 L32 6 L60 30"/><path d="M11 25 V58 H53 V25"/><rect x="25" y="38" width="14" height="20"/><rect x="15" y="32" width="8" height="8"/><rect x="41" y="32" width="8" height="8"/><rect x="27" y="22" width="10" height="8"/></svg>
    <h3>Residential</h3>
    <p>Nullam ultrices placerat libero, in tristique massa euismod eget. Suspendisse semper sapien</p>
  </div>
  <div class="service" style="left:448px">
    <svg width="64" height="62" viewBox="0 0 64 62" fill="none" stroke="#fff" stroke-width="2.5"><rect x="6" y="4" width="52" height="8"/><path d="M4 12 H60 L56 22 H8 Z"/><path d="M10 22 V58 H54 V22"/><rect x="16" y="32" width="12" height="26"/><rect x="34" y="32" width="14" height="14"/><circle cx="41" cy="39" r="3"/></svg>
    <h3>Commercial</h3>
    <p>Nullam ultrices placerat libero, in tristique massa euismod eget. Suspendisse semper sapien</p>
  </div>
  <div class="service" style="left:808px">
    <svg width="94" height="62" viewBox="0 0 94 62" fill="none" stroke="#fff" stroke-width="2.5"><path d="M4 8 H84 Q90 8 90 14 V46 H4 Z"/><rect x="10" y="14" width="18" height="14"/><rect x="32" y="14" width="18" height="14"/><rect x="54" y="14" width="14" height="26"/><rect x="72" y="14" width="12" height="14"/><circle cx="22" cy="48" r="6"/><circle cx="72" cy="48" r="6"/></svg>
    <h3>Transportation</h3>
    <p>Nullam ultrices placerat libero, in tristique massa euismod eget. Suspendisse semper sapien</p>
  </div>
  <div class="dots light" style="top:166px"><i></i><i class="on"></i><i></i><i></i><i></i></div>
</section>

<section class="approach">
  <div class="abs photo" role="img" aria-label="Photo of a team in white protective suits carrying disinfectant containers"></div>
  <h2 class="abs">Our Approach</h2>
  <p class="abs para p1">Lorem ipsum dolor sit amet, consectetur adipiscing elit. Integer auctor feugiat libero vitae tincidunt. Ut varius malesuada ex at porta. Quisque augue mauris, dignissim sed velit eget, finibus porta urna. Suspendisse eget tempor risus, et imperdiet nisi.</p>
  <p class="abs para p2">Proin rhoncus, tellus sagittis rutrum aliquam, est ipsum vestibulum leo, vel tempor orci lacus ut nunc. Vivamus aliquet lectus nisl, vitae efficitur nisl dignissim quis.</p>
  <div class="dots" style="top:189px"><i></i><i></i><i class="on"></i><i></i><i></i></div>
</section>

<section class="banner">
  <div class="abs" role="img" aria-label="Close-up photo of a gloved hand holding a green fogging machine, with orange tint" style="inset:0"></div>
  <h2 class="abs center">We provide a service to electronically measure cleanliness of any surface<br>and a value added disinfecting fogging surface.</h2>
  <p class="abs para">Lorem ipsum dolor sit amet, consectetur adipiscing elit. Integer auctor feugiat libero vitae tincidunt. Ut varius malesuada ex at porta. Quisque augue mauris, dignissim sed velit eget, finibus porta urna. Suspendisse eget tempor risus, et imperdiet nisi. Proin rhoncus, tellus sagittis rutrum aliquam, est ipsum vestibulum leo, vel tempor orci lacus ut nunc. Vivamus aliquet lectus nisl, vitae efficitur nisl dignissim quis.</p>
</section>

<section class="reviews">
  <h2 class="abs center">What People are Saying</h2>
  <p class="abs center sub">Lorem ipsum dolor sit amet, consectetur adipiscing elit. Integer auctor feugiat libero vitae tincidunt.</p>
  <div class="card" style="left:74px"><div class="q"><svg width="46" height="38" viewBox="0 0 46 38"><path fill="#f26522" d="M2 18 Q2 4 16 0 L18 5 Q10 8 10 15 H20 V38 H2 Z M26 18 Q26 4 40 0 L42 5 Q34 8 34 15 H44 V38 H26 Z"/></svg></div><p>&ldquo; Lorem ipsum dolor sit amet, consectetur adipiscing elit. Integer auctor feugiat libero vitae tincidunt. Ut varius malesuada ex at porta maximus nisl ante, ut dictum felis luctus..&rdquo;</p></div>
  <div class="card" style="left:435px"><div class="q"><svg width="46" height="38" viewBox="0 0 46 38"><path fill="#f26522" d="M2 18 Q2 4 16 0 L18 5 Q10 8 10 15 H20 V38 H2 Z M26 18 Q26 4 40 0 L42 5 Q34 8 34 15 H44 V38 H26 Z"/></svg></div><p>&ldquo; Lorem ipsum dolor sit amet, consectetur adipiscing elit. Integer auctor feugiat libero vitae tincidunt. Ut varius malesuada ex at porta maximus nisl ante, ut dictum felis luctus..&rdquo;</p></div>
  <div class="card" style="left:796px"><div class="q"><svg width="46" height="38" viewBox="0 0 46 38"><path fill="#f26522" d="M2 18 Q2 4 16 0 L18 5 Q10 8 10 15 H20 V38 H2 Z M26 18 Q26 4 40 0 L42 5 Q34 8 34 15 H44 V38 H26 Z"/></svg></div><p>&ldquo; Lorem ipsum dolor sit amet, consectetur adipiscing elit. Integer auctor feugiat libero vitae tincidunt. Ut varius malesuada ex at porta maximus nisl ante, ut dictum felis luctus..&rdquo;</p></div>
  <div class="who" style="left:74px"><b>Name Heading</b><div class="stars">★★★★★</div></div>
  <div class="who" style="left:435px"><b>Name Heading</b><div class="stars">★★★★★</div></div>
  <div class="who" style="left:796px"><b>Name Heading</b><div class="stars">★★★★★</div></div>
  <div class="dots" style="top:220px"><i></i><i></i><i></i><i class="on"></i><i></i></div>
</section>

<section class="contact">
  <div class="abs" role="img" aria-label="Dark blue background photo with faint chemical structure formulas" style="inset:0"></div>
  <h2 class="abs center">Contact Us</h2>
  <div class="abs center line">
    <svg width="13" height="13" viewBox="0 0 24 24"><path fill="#fff" d="M6.6 10.8a15 15 0 0 0 6.6 6.6l2.2-2.2c.3-.3.7-.4 1-.2 1.1.4 2.3.6 3.6.6.6 0 1 .4 1 1V20c0 .6-.4 1-1 1A17 17 0 0 1 3 4c0-.6.4-1 1-1h3.5c.6 0 1 .4 1 1 0 1.3.2 2.5.6 3.6.1.3 0 .7-.2 1z"/></svg>
    <span>1-800-555-0142</span><span>|</span>
    <svg width="14" height="11" viewBox="0 0 14 11"><rect width="14" height="11" rx="1" fill="#fff"/><path d="M1 1 L7 6 L13 1" fill="none" stroke="#2d3a48" stroke-width="1.4"/></svg>
    <span>info@treldmist.com</span>
  </div>
  <div class="field" style="top:179px;height:35px">Name</div>
  <div class="field" style="top:226px;height:36px">Email Address</div>
  <div class="field" style="top:272px;height:36px">Phone</div>
  <div class="field" style="top:320px;height:122px">Message</div>
  <div class="submit">Submit</div>
  <div class="dots light" style="top:218px"><i></i><i></i><i></i><i></i><i style="background:#cfcfcf"></i></div>
</section>

<footer class="foot">
  <div class="logo"><span class="mark"></span>TRELDMIST</div>
  <p class="col" style="left:342px;top:58px;width:240px">Nullam ultrices placerat libero, in tristique massa euismod eget. Suspendisse semper sapien eget enim sed mauris.</p>
  <p class="col" style="left:646px;top:58px">220 Harlow Quay Street<br>Marlinford, CA 94200</p>
  <p class="col" style="left:646px;top:128px;display:flex;gap:14px;align-items:center"><svg width="12" height="12" viewBox="0 0 24 24"><path fill="#333" d="M6.6 10.8a15 15 0 0 0 6.6 6.6l2.2-2.2c.3-.3.7-.4 1-.2 1.1.4 2.3.6 3.6.6.6 0 1 .4 1 1V20c0 .6-.4 1-1 1A17 17 0 0 1 3 4c0-.6.4-1 1-1h3.5c.6 0 1 .4 1 1 0 1.3.2 2.5.6 3.6.1.3 0 .7-.2 1z"/></svg>555-017-2288</p>
  <div class="social" aria-label="Social media links"><i></i><i></i></div>
  <p class="abs center copy">Copyright © 2020 Treldmist All rights reserved.</p>
</footer>

</body>
</html>
```